Medical Device Packaging Project 2 of 5

We are a medical device startup company needing packaging for a total of 5 device brands. This is posting 2 of 5 and the device name is "Venmira"

Venmira is an intraocular lens for use in cataract surgery. The target market is Chinese ophthalmologists. The box should be sophisticated and upmarket.

The company name is Tordel Vision, I have included the logo in the uploaded files section. You should include the logo on the box.

I have uploaded a sample lens boxes from other companies that demonstrate the information needed to be contained on the box in terms of address, warnings, symbols, etc.

I have also uploaded the blank dieline of the boxes

You are welcome and encouraged to also submit to projects 1, 3, 4, and 5 as well. The same rules and expectations apply.

Industry/Entity Type

It Company

Requirements
Should not have
• Should not have any images of an eye or any bionic/futuristic feel to the design
• Note that the stavolens box is for text reference only. You may use the lens image but the futuristic/bionic look is NOT what we are going for with this brand. It should be traditional upmarket medical device artwork.

```html
<!DOCTYPE html>
<html lang="en">
<head>
<meta charset="utf-8">
<title>Venmira – Intraocular Lens Carton Dieline</title>
<link rel="stylesheet" href="https://fonts.googleapis.com/css2?family=Great+Vibes&family=Open+Sans:ital,wght@0,400;0,600;0,700;1,700&family=Tinos&display=swap">
<style>
  :root {
    --paper: #ffffff;
    --carton: #fde3a6;
    --carton-cloud: #fdebc2;
    --cut-line: #3a3a3a;
    --ink: #1a1a1a;
    --brand-blue: #1d4f8f;
    --dim-ink: #444444;
  }
  html, body {
    margin: 0;
    padding: 0;
    width: 1200px;
    height: 848px;
    overflow: hidden;
    background: var(--paper);
  }
  .sheet {
    position: relative;
    width: 1200px;
    height: 848px;
    font-family: "Open Sans", Arial, sans-serif;
    color: var(--ink);
  }
  .dieline {
    position: absolute;
    left: 0;
    top: 0;
  }
  .dim {
    position: absolute;
    font-family: "Tinos", "Times New Roman", serif;
    font-size: 10px;
    color: var(--dim-ink);
    white-space: nowrap;
  }
  .dim--vertical { transform: rotate(-90deg); transform-origin: left top; }

  .product-name {
    position: absolute;
    left: 468px;
    top: 170px;
    font-family: "Great Vibes", cursive;
    font-size: 62px;
    line-height: 1;
    color: var(--ink);
  }
  .edge-claim {
    position: absolute;
    left: 463px;
    top: 240px;
    font-weight: 700;
    font-size: 16px;
    letter-spacing: -0.2px;
  }
  .brand-name {
    position: absolute;
    font-weight: 700;
    color: var(--brand-blue);
    white-space: nowrap;
    text-transform: uppercase;
    text-align: center;
  }
  .brand-name span { display: block; }
  .brand-name--front {
    left: 596px; top: 292px; width: 176px;
    font-size: 28px; line-height: 31px; letter-spacing: 3px;
  }
  .brand-name--side-flap {
    left: 440px; top: 440px; width: 100px;
    font-size: 15px; line-height: 17px; letter-spacing: 2px;
  }
  .brand-name--side-panel {
    left: 860px; top: 296px; width: 100px;
    font-size: 15px; line-height: 17px; letter-spacing: 2px;
    transform: rotate(90deg); transform-origin: left top;
  }
  .front-descriptor {
    position: absolute;
    left: 621px;
    top: 380px;
    font-weight: 700;
    font-size: 14px;
  }
  .flap-descriptor {
    position: absolute;
    left: 566px;
    top: 444px;
    font-weight: 700;
    font-style: italic;
    font-size: 14px;
    line-height: 17px;
  }
  .address {
    position: absolute;
    left: 688px;
    top: 118px;
    font-weight: 700;
    font-size: 10px;
    transform: rotate(180deg);
  }
  .label-copy {
    position: absolute;
    left: 446px;
    top: 516px;
    font-size: 7.2px;
    line-height: 9.4px;
  }
  .label-copy p { margin: 0 0 4.2px 0; }
  .sterile-mark {
    position: absolute;
    left: 443px;
    top: 713px;
    display: flex;
    border: 1px solid var(--ink);
    font-size: 8px;
    font-weight: 700;
    height: 16px;
    line-height: 16px;
  }
  .sterile-mark span { padding: 0 4px; }
  .sterile-mark span + span { border-left: 1px solid var(--ink); }
</style>
</head>
<body>
<main class="sheet">
  <svg class="dieline" width="1200" height="848" viewBox="0 0 1200 848" role="img" aria-label="Carton dieline printed with a soft pale-yellow traditional cloud pattern">
    <g class="carton-print" fill="var(--carton)">
      <path d="M328 45 H872 V145 H328 Z"/>
      <path d="M318 140 H894 V420 H318 Z"/>
      <path d="M328 405 H872 V505 H328 Z"/>
      <path d="M407 495 H806 V815 H407 Z"/>
    </g>
    <g class="cut-lines" fill="none" stroke="var(--cut-line)" stroke-width="0.8">
      <path d="M427 140 V58 Q427 52 433 52 H782 Q788 52 788 58 V140"/>
      <path d="M427 140 L410 132 H340 V72 L427 58"/>
      <path d="M788 140 L805 132 H870 V72 L788 58"/>
      <path d="M325 152 H887 M325 405 H887"/>
      <path d="M325 152 V405 M427 140 V505 M788 140 V505 M887 152 V405"/>
      <path d="M325 152 L310 140 M887 152 L902 140"/>
      <path d="M325 152 H285 Q275 152 275 162 V395 Q275 405 285 405 H325"/>
      <path d="M887 152 H927 Q937 152 937 162 V395 Q937 405 927 405 H887"/>
      <path d="M427 418 L410 418 H340 V480 L427 497"/>
      <path d="M788 418 L805 418 H870 V480 L788 497"/>
      <path d="M427 505 H788 M407 505 V760 H806 V505"/>
      <path d="M427 760 V795 H788 V760"/>
    </g>
    <g class="regulatory-icons" fill="none" stroke="var(--ink)" stroke-width="0.9">
      <circle cx="863" cy="167" r="6"/><path d="M858 172 L868 162"/>
      <circle cx="863" cy="199" r="6"/><path d="M858 204 L868 194 M860 199 H866"/>
      <circle cx="863" cy="230" r="6"/><path d="M858 235 L868 225"/>
      <path d="M863 253 L869 265 H857 Z M863 257 V261"/>
      <path d="M522 715 L531 731 H513 Z M522 720 V726"/>
      <circle cx="553" cy="723" r="7.5"/><path d="M547 729 L559 717"/>
      <circle cx="584" cy="723" r="7.5"/><path d="M578 729 L590 717 M580 723 H588"/>
      <circle cx="613" cy="723" r="7.5"/><path d="M607 729 L619 717"/>
    </g>
  </svg>

  <span class="dim" style="left:372px;top:31px">35mm</span>
  <span class="dim" style="left:576px;top:37px">128mm</span>
  <span class="dim" style="left:813px;top:31px">35mm</span>
  <span class="dim" style="left:286px;top:127px">18mm</span>
  <span class="dim" style="left:898px;top:127px">18mm</span>
  <span class="dim dim--vertical" style="left:306px;top:112px">35mm</span>
  <span class="dim dim--vertical" style="left:258px;top:292px">90mm</span>
  <span class="dim dim--vertical" style="left:314px;top:462px">35mm</span>
  <span class="dim dim--vertical" style="left:394px;top:656px">90mm</span>
  <span class="dim dim--vertical" style="left:394px;top:797px">12mm</span>

  <div class="address">Address here....</div>

  <div class="product-name">Venmira</div>
  <div class="edge-claim">With 360˚Square Edge</div>
  <div class="brand-name brand-name--front"><span>Tordel</span><span>Vision</span></div>
  <div class="front-descriptor">Intraocular lens</div>
  <div class="brand-name brand-name--side-panel"><span>Tordel</span><span>Vision</span></div>

  <div class="brand-name brand-name--side-flap"><span>Tordel</span><span>Vision</span></div>
  <div class="flap-descriptor">Intraocular lens<br>With 360˚Square Edge</div>

  <div class="label-copy">
    <p>Contains one sterile intraocular lens<br>Do not use if the packing is damaged<br>Do not resterilize</p>
    <p>Contains one sterile intraocular lens<br>Do not use if the packing is damaged<br>Do not resterilize</p>
    <p>Contains one sterile intraocular lens<br>Do not use if the packing is damaged<br>Do not resterilize</p>
    <p>Contains one sterile intraocular lens<br>Do not use if the packing is damaged<br>Do not resterilize</p>
    <p>Contains one sterile intraocular lens<br>Do not use if the packing is damaged<br>Do not resterilize</p>
    <p>Contains one sterile intraocular lens<br>Do not use if the packing is damaged<br>Do not resterilize</p>
  </div>
  <div class="sterile-mark"><span>STERILE</span><span>EO</span></div>
</main>
</body>
</html>
```